Silver Heron Construction Services

Create a business card for my business consulting company
Danielle Vesk, Founder and CEO
4816 Alder Brook Way, Ste 100
Denver, CO. 80451
303.782.4190 cell
dvesk@silverheronconst.example
www.silverheronconst.example

Target Market(s)

Private Equity and Construction Companies

Industry/Entity Type

Business / Sales Consulting

Contact Information for Business Card

Tag Line that says "Where The Road To Success Is Always Under Construction"

Requirements
Must have
• Logo on both sides of the card.
Nice to have
• Add tagline to the same side of the card as my name and contact info

```html
<!DOCTYPE html>
<html lang="en">
<head>
<meta charset="UTF-8">
<title>Silver Heron Construction Services – Business Card</title>
<link href="https://fonts.googleapis.com/css2?family=Open+Sans:wght@400;700;800&display=swap" rel="stylesheet">
<style>
  :root {
    --ink: #111111;
    --paper: #ffffff;
    --paper-shade: #f1f1f1;
    --text-grey: #555555;
    --backdrop: #d9d6d2;
    --illustration-dark: #1a1a1a;
    --illustration-mid: #4a4a4a;
  }
  * { box-sizing: border-box; margin: 0; padding: 0; }
  html, body {
    width: 1200px; height: 900px; overflow: hidden;
    background: var(--backdrop);
    font-family: "Open Sans", Arial, sans-serif;
  }
  .stage {
    width: 1200px; height: 900px;
    display: flex; flex-direction: column; align-items: center; justify-content: center;
    gap: 40px;
  }
  .card {
    position: relative;
    width: 640px; height: 370px;
    background: linear-gradient(135deg, var(--paper-shade) 0%, var(--paper) 60%);
    overflow: hidden;
    box-shadow: 0 6px 18px rgba(0,0,0,0.25);
  }
  .brand {
    position: absolute; top: 40px; right: 60px;
    display: flex; align-items: center; gap: 12px;
    color: var(--ink);
    font-weight: 800; font-size: 17px; line-height: 1.15;
    text-transform: uppercase; letter-spacing: 0.5px;
  }
  .brand-mark { width: 22px; height: 22px; background: var(--ink); flex: none; }
  .band {
    position: absolute; left: 0; right: 0; bottom: 0;
    height: 64px; background: var(--ink);
  }
  .scenery {
    position: absolute; bottom: 64px;
    width: 150px; height: 56px;
    background: linear-gradient(180deg, var(--illustration-mid), var(--illustration-dark));
  }
  .card-front .scenery { left: 0; }
  .card-back .scenery { right: 0; }

  .contact-block {
    position: absolute; left: 40px; bottom: 80px;
    color: var(--text-grey);
  }
  .person-name {
    color: var(--ink); font-weight: 800; font-size: 19px; line-height: 1.3;
    text-transform: uppercase; letter-spacing: 0.3px;
  }
  .person-title { font-size: 16px; line-height: 1.3; margin-bottom: 12px; }
  .contact-list { list-style: none; padding-left: 22px; }
  .contact-list li {
    display: flex; align-items: center; gap: 10px;
    font-size: 15px; line-height: 1.6; white-space: nowrap;
  }
  .contact-list svg { width: 15px; height: 15px; fill: var(--ink); flex: none; }
  .tagline {
    position: absolute; left: 40px; bottom: 0; height: 64px;
    display: flex; align-items: center;
    color: var(--paper); font-weight: 700; font-size: 19px;
  }
</style>
</head>
<body>
<main class="stage">

  <section class="card card-front" aria-label="Card front">
    <div class="brand">
      <span class="brand-mark"></span>
      <span>Silver Heron<br>Construction Services</span>
    </div>
    <div class="scenery" role="img" aria-label="Illustration area: mountain and rooftop scenery"></div>
    <div class="band"></div>
  </section>

  <section class="card card-back" aria-label="Card back">
    <div class="brand">
      <span class="brand-mark"></span>
      <span>Silver Heron<br>Construction Services</span>
    </div>
    <div class="scenery" role="img" aria-label="Illustration area: mountain and rooftop scenery"></div>

    <div class="contact-block">
      <p class="person-name">Danielle Vesk</p>
      <p class="person-title">Founder and CEO</p>
      <ul class="contact-list">
        <li>
          <svg viewBox="0 0 24 24" aria-hidden="true"><path d="M6.6 10.8a15.1 15.1 0 0 0 6.6 6.6l2.2-2.2a1 1 0 0 1 1-.25 11.4 11.4 0 0 0 3.6.57 1 1 0 0 1 1 1V20a1 1 0 0 1-1 1A17 17 0 0 1 3 4a1 1 0 0 1 1-1h3.5a1 1 0 0 1 1 1c0 1.25.2 2.45.57 3.57a1 1 0 0 1-.25 1z"/></svg>
          303.782.4190
        </li>
        <li>
          <svg viewBox="0 0 24 24" aria-hidden="true"><path d="M2 5h20v14H2z M2 5l10 8 10-8" fill="none" stroke="#111" stroke-width="2"/></svg>
          dvesk@silverheronconst.example
        </li>
        <li>
          <svg viewBox="0 0 24 24" aria-hidden="true"><circle cx="12" cy="12" r="9" fill="none" stroke="#111" stroke-width="2"/><path d="M3 12h18M12 3c3 3 3 15 0 18M12 3c-3 3-3 15 0 18" fill="none" stroke="#111" stroke-width="1.6"/></svg>
          www.silverheronconst.example
        </li>
        <li>
          <svg viewBox="0 0 24 24" aria-hidden="true"><path d="M12 2a7 7 0 0 0-7 7c0 5.25 7 13 7 13s7-7.75 7-13a7 7 0 0 0-7-7zm0 9.5a2.5 2.5 0 1 1 0-5 2.5 2.5 0 0 1 0 5z"/></svg>
          4816 Alder Brook Way, Ste 100, Denver, CO. 80451
        </li>
      </ul>
    </div>

    <div class="band"></div>
    <p class="tagline">The Road To Success Is Always Under Construction</p>
  </section>

</main>
</body>
</html>
```